Design a Website Mockup for Subscription Luxury website

A subscription based luxury marketplace similar to Karvell showcase. Name of site is [login to view URL]

```html
<!DOCTYPE html>
<html lang="en">
<head>
<meta charset="utf-8">
<title>Crownhaven – Luxury Marketplace</title>
<link href="https://fonts.googleapis.com/css2?family=Cabin:wght@400;500&family=Roboto:wght@400&display=swap" rel="stylesheet">
<style>
:root{
  --page:#262626;
  --column:#1b1b1b;
  --header:#161616;
  --tab:#0d0d0d;
  --tab-active:#2a2a2a;
  --tab-border:#5a5a5a;
  --text:#bdbdbd;
  --heading:#c9c9c9;
  --white:#f2f2f2;
  --frame:#9a9a9a;
  --footer-band:#3a3a3a;
}
*{box-sizing:border-box;margin:0;padding:0}
html,body{width:813px;height:1200px;overflow:hidden}
body{background:var(--page);font-family:"Roboto",Arial,sans-serif;position:relative}
.column{position:absolute;left:94px;top:0;width:625px;height:1200px;background:var(--column)}
.site-header{position:absolute;left:0;top:0;width:625px;height:66px;background:var(--header)}
.brand{position:absolute;left:5px;top:6px;font-family:"Cabin",sans-serif;font-size:38px;font-weight:500;color:#d6d6d6;letter-spacing:.3px}
.phone{position:absolute;right:6px;top:16px;font-family:"Cabin",sans-serif;font-size:17px;color:var(--white)}
.main-nav{position:absolute;left:0;top:66px;width:625px;height:49px;display:flex}
.main-nav a{display:block;height:49px;border:2px solid var(--tab-border);background:linear-gradient(#1e1e1e,var(--tab));text-align:center;color:var(--white);text-decoration:none}
.main-nav a.active{background:linear-gradient(#3a3a3a,var(--tab-active))}
.main-nav .label{display:block;font-family:"Cabin",sans-serif;font-size:16px;margin-top:4px}
.main-nav .sub{display:block;font-family:"Cabin",sans-serif;font-size:8.5px;color:#cfcfcf;margin-top:5px}
.hero{position:absolute;left:0;top:115px;width:625px;height:314px;background:linear-gradient(180deg,#7a5236 0%,#b9a8a6 30%,#8aa3bd 45%,#a2877a 65%,#6b4a36 100%)}
.slider-dots{position:absolute;left:284px;top:435px;display:flex;gap:5px}
.slider-dots span{width:7px;height:7px;border-radius:50%;background:#cfcfcf}
.slider-dots span.on{background:#f5f5f5;box-shadow:0 0 2px #fff}
.divider{position:absolute;left:0;top:463px;width:625px;height:8px}
.divider i{position:absolute;top:0;height:1px;background:#5a5a5a}
.ornament{position:absolute;left:282px;top:455px;width:62px;height:22px;background:#4a4a4a;border-radius:4px}
.section-title{position:absolute;left:0;top:497px;width:625px;text-align:center;font-family:"Cabin",sans-serif;font-size:21px;color:#b8b8b8}
.feature-photo{position:absolute;width:305px;height:166px;border:2px solid var(--frame)}
.feature-text{position:absolute;width:302px}
.feature-text h2{font-family:"Cabin",sans-serif;font-weight:400;font-size:14px;color:var(--heading);margin-bottom:9px;white-space:nowrap}
.feature-text p{font-size:8.1px;line-height:13px;color:var(--text)}
.footer-nav{position:absolute;left:0;top:1131px;width:625px;height:26px;background:linear-gradient(#4a4a4a,#2e2e2e);display:flex;justify-content:center;align-items:center;gap:0;font-size:8.4px;color:#e4e4e4;white-space:nowrap}
.footer-nav span.sep{margin:0 7px}
.copyright{position:absolute;left:8px;top:1175px;font-size:8.2px;color:#bdbdbd}
.copyright u{color:#d0d0d0}
.social{position:absolute;right:6px;top:1170px;display:flex;gap:10px}
.social span{width:16px;height:16px;background:#8a8a8a;border-radius:3px}
</style>
</head>
<body>
<div class="column">
  <header class="site-header">
    <div class="brand">Crownhaven</div>
    <div class="phone">Phone 410.282.75</div>
  </header>

  <nav class="main-nav">
    <a href="#" style="width:221px"><span class="label">Auto’s</span><span class="sub">A Luxury Marketplace Of AutoMobiles</span></a>
    <a href="#" class="active" style="width:200px"><span class="label">Home’s</span><span class="sub">A Luxury Marketplace Of Homes</span></a>
    <a href="#" style="width:204px"><span class="label">Boat’s</span><span class="sub">A Luxury Marketplace Of Boats</span></a>
  </nav>

  <div class="hero" role="img" aria-label="Luxury villa living room with vaulted wooden ceiling, columns and panoramic desert view"></div>

  <div class="slider-dots"><span class="on"></span><span></span><span></span><span></span></div>

  <div class="divider"><i style="left:0;width:282px"></i><i style="left:0;width:282px;top:4px"></i><i style="left:344px;width:281px"></i><i style="left:344px;width:281px;top:4px"></i></div>
  <div class="ornament" role="img" aria-label="Decorative flourish"></div>

  <h1 class="section-title">The World’s Premier Luxury Marketplace</h1>

  <div class="feature-photo" style="left:8px;top:538px;background:linear-gradient(160deg,#a9a9a9,#6d6d6d 55%,#8f1a1f 60%,#5e5e5e)" role="img" aria-label="Red luxury coupe on grey pavement"></div>
  <div class="feature-text" style="left:318px;top:536px">
    <h2>AUTOS - A Luxury marketplace of &nbsp;Automobiles</h2>
    <p>There are many variations of passages of Lorem Ipsum available, but the majority have suffered alteration in some form, by injected humour, or randomised words which don't look even slightly believable. If you are going to use a passage of Lorem Ipsum, you need to be sure there isn't anything embarrassing hidden in the middle of text. All the Lorem Ipsum generators on the Internet tend to repeat predefined chunks as necessary, making this the first true generator on the Internet. It uses a dictionary of over 200 Latin words, combined with a handful of model sentence structures, to generate Lorem Ipsum which looks reasonable. The generated Lorem Ipsum is therefore always free from repetition, injected humour, or non-characteristic words etc.</p>
  </div>

  <div class="feature-text" style="left:8px;top:730px">
    <h2>AUTOS - A Luxury marketplace of &nbsp;Home’s</h2>
    <p>There are many variations of passages of Lorem Ipsum available, but the majority have suffered alteration in some form, by injected humour, or randomised words which don't look even slightly believable. If you are going to use a passage of Lorem Ipsum, you need to be sure there isn't anything embarrassing hidden in the middle of text. All the Lorem Ipsum generators on the Internet tend to repeat predefined chunks as necessary, making this the first true generator on the Internet. It uses a dictionary of over 200 Latin words, combined with a handful of model sentence structures, to generate Lorem Ipsum which looks reasonable. The generated Lorem Ipsum is therefore always free from repetition, injected humour, or non-characteristic words etc.</p>
  </div>
  <div class="feature-photo" style="left:314px;top:735px;background:linear-gradient(180deg,#8fb6d8,#c9a58f 50%,#8a5a44 80%,#3d3a2a)" role="img" aria-label="Mediterranean-style mansion with palm trees at dusk"></div>

  <div class="feature-photo" style="left:8px;top:929px;background:linear-gradient(150deg,#2c8a80,#e8ecef 45%,#c9d2d8 60%,#2f8f85)" role="img" aria-label="White sailing yacht on turquoise water"></div>
  <div class="feature-text" style="left:318px;top:922px">
    <h2>AUTOS - A Luxury marketplace of &nbsp;Boat’s</h2>
    <p>There are many variations of passages of Lorem Ipsum available, but the majority have suffered alteration in some form, by injected humour, or randomised words which don't look even slightly believable. If you are going to use a passage of Lorem Ipsum, you need to be sure there isn't anything embarrassing hidden in the middle of text. All the Lorem Ipsum generators on the Internet tend to repeat predefined chunks as necessary, making this the first true generator on the Internet. It uses a dictionary of over 200 Latin words, combined with a handful of model sentence structures, to generate Lorem Ipsum which looks reasonable. The generated Lorem Ipsum is therefore always free from repetition, injected humour, or non-characteristic words etc.</p>
  </div>

  <nav class="footer-nav">
    <span>Autos</span><span class="sep">•</span><span>Homes</span><span class="sep">•</span><span>Boats</span><span class="sep">•</span><span>Gulf Coast Living Magazine</span><span class="sep">•</span><span>Car News</span><span class="sep">•</span><span>Celebrity Car</span><span class="sep">•</span><span>Subscriptions</span><span class="sep">•</span><span>Site Map</span><span class="sep">•</span><span>Autos RSS</span><span class="sep">•</span><span>Boats RSS</span>
  </nav>

  <div class="copyright"><u>Crownhaven</u> © 2014. All Rights Reserved.</div>
  <div class="social" aria-label="Social links"><span></span><span></span><span></span><span></span></div>
</div>
</body>
</html>
```